Software allocation system needs a business card design

We need a business card designed for our software platform - www.rostellio.com.au

At the moment the logo and website is all black and white, we are happy for suggestions on implementing some colour throughout either the logo or business card.

Industry/Entity Type

Software

Font styles to use
Sans Serif

Colors

Designer to choose colors to be used in the design.

```html
<!DOCTYPE html>
<html lang="en">
<head>
<meta charset="utf-8">
<title>Rostellio Business Card</title>
<link href="https://fonts.googleapis.com/css2?family=Questrial&display=swap" rel="stylesheet">
<style>
  :root {
    --backdrop: #3b3b3d;
    --brand-red: #8c1519;
    --deep-red: #7a1114;
    --ink: #1c1c1c;
    --paper: #ffffff;
    --muted: #444444;
  }
  * { margin: 0; padding: 0; box-sizing: border-box; }
  html, body { width: 1200px; height: 946px; overflow: hidden; }
  body {
    background: var(--backdrop);
    font-family: "Questrial", "Century Gothic", sans-serif;
    position: relative;
  }
  .card {
    position: absolute;
    width: 700px;
    height: 400px;
    overflow: hidden;
    box-shadow: 0 14px 30px rgba(0,0,0,.45);
  }
  /* Back side */
  .card--back {
    left: 80px; top: 50px;
    background: linear-gradient(135deg, var(--brand-red), var(--deep-red));
    color: var(--paper);
  }
  .card--back .wordmark {
    position: absolute; left: 0; right: 0; top: 150px;
    text-align: center;
    font-size: 56px; letter-spacing: 8px; color: var(--paper);
  }
  .card--back .web {
    position: absolute; left: 0; right: 0; top: 232px;
    text-align: center; font-size: 19px; letter-spacing: 1px;
  }
  /* Front side */
  .card--front { left: 420px; top: 490px; background: var(--paper); color: var(--ink); }
  .card--front .decor { position: absolute; inset: 0; }
  .brand {
    position: absolute; left: 56px; top: 96px;
    display: flex; align-items: center; gap: 14px;
  }
  .brand .dot { width: 22px; height: 22px; border-radius: 50%; background: var(--brand-red); }
  .brand .wordmark { font-size: 52px; letter-spacing: 7px; color: var(--ink); }
  .person { position: absolute; right: 60px; top: 52px; text-align: right; }
  .person .name { color: var(--brand-red); font-size: 19px; font-weight: bold; letter-spacing: .5px; }
  .person .title { font-size: 12px; color: var(--muted); }
  .address {
    position: absolute; left: 110px; top: 196px;
    font-size: 20px; line-height: 22px; color: var(--muted);
  }
  .contacts {
    position: absolute; left: 110px; top: 258px;
    list-style: none; font-size: 20px; line-height: 26px; color: var(--ink);
  }
  .contacts li { display: flex; align-items: center; gap: 10px; }
  .contacts svg { width: 16px; height: 16px; fill: var(--brand-red); flex: none; }
  .card--front .web {
    position: absolute; right: 22px; top: 324px;
    color: var(--paper); font-size: 17px; letter-spacing: .5px;
    white-space: nowrap;
  }
</style>
</head>
<body>
  <section class="card card--back">
    <div class="wordmark">ROSTELLIO</div>
    <div class="web">www.rostellio.com.au</div>
  </section>

  <section class="card card--front">
    <svg class="decor" viewBox="0 0 700 400" aria-hidden="true">
      <polygon points="0,374 450,356 450,400 0,400" fill="#8c1519"/>
      <polygon points="0,382 450,365 450,369 0,386" fill="#6c0f12"/>
      <polygon points="480,298 700,258 700,400 450,400 450,330 480,330" fill="#1c1c1c"/>
      <rect x="0" y="238" width="18" height="16" fill="#8c1519"/>
      <rect x="18" y="254" width="18" height="16" fill="#1c1c1c"/>
    </svg>
    <div class="brand"><span class="dot"></span><span class="wordmark">ROSTELLIO</span></div>
    <div class="person">
      <div class="name">NOAH BRENT</div>
      <div class="title">Job Title</div>
    </div>
    <div class="address">PO Box 712<br>Harbour Vale NSW 2140</div>
    <ul class="contacts">
      <li><svg viewBox="0 0 16 16"><path d="M4 1h8a1 1 0 0 1 1 1v12a1 1 0 0 1-1 1H4a1 1 0 0 1-1-1V2a1 1 0 0 1 1-1zm1 2v9h6V3z"/></svg>412-555-0193</li>
      <li><svg viewBox="0 0 16 16"><path d="M4 1h7v4H4zM2 6h12v8H2zm3 2v2h6V8z"/></svg>612-555-0148</li>
      <li><svg viewBox="0 0 16 16"><path d="M1 3h14v10H1zm1.5 1.5L8 9l5.5-4.5z"/></svg>hello@rostellio.com.au</li>
    </ul>
    <div class="web">www.rostellio.com.au</div>
  </section>
</body>
</html>
```